Reminder card

We are an alternative health clinic. This project is for a postcard. The postcard is sent to our clients to remind them they have not been in the clinic for a long time and it's time for them to make an appointment. Our website is MeadowbrookWellness.com
Updates

Target Market(s)

Our clients are usually adults between the ages of 35 - 55, 70% women, 30% men. These are educated, wealthy, people who are committed to their health. Our clients expect us to be professional and an authority in our field, but friendly, playful and open.

Industry/Entity Type

Health

Font styles to use
Other font styles liked:
• our name is blackjack and the rest of the website is open sans

Requirements
Must have
• The front of the postcard must have our logo and name (see attached).

The front of the post card must have this text:
Feel good and want to stay that way? Need a boost? It's time for your tune-up appointment at Meadowbrook Wellness.

The right side on the back of the card must be blank for an address and stamp.

The left side on the back of the card must have our phone number (415.627.1943) and website (MeadowbrookWellness.com).
Nice to have
• We have an egg theme in our office. Our website is MeadowbrookWellness.com and if you look at it, you'll see the pictures of them.

The postcard should be in the same style as the website in color and tone.
Should not have
• We want things to be playful, but not look like something for children.

```html
<!DOCTYPE html>
<html lang="en">
<head>
<meta charset="utf-8">
<title>Meadowbrook Wellness – Reminder Postcard</title>
<link href="https://fonts.googleapis.com/css2?family=Open+Sans:wght@400;600&family=Yellowtail&display=swap" rel="stylesheet">
<style>
  :root {
    --leaf: #5f8f1f;
    --leaf-dark: #44701a;
    --paper: #ffffff;
    --ink: #2b2b2b;
    --muted: #6a6a6a;
    --backdrop: #e6e6e6;
    --shell: #e9a27a;
    --sprout: #7dbb2c;
    --rule: #d8d8d8;
  }
  * { box-sizing: border-box; margin: 0; padding: 0; }
  html, body { width: 1200px; height: 800px; overflow: hidden; }
  body {
    background: var(--backdrop);
    font-family: "Open Sans", Arial, sans-serif;
    color: var(--ink);
    position: relative;
  }
  .postcard {
    position: absolute;
    top: 220px;
    width: 540px;
    height: 360px;
    background: var(--paper);
    overflow: hidden;
    box-shadow: 0 6px 18px rgba(0,0,0,0.12);
  }
  .postcard--front { left: 50px; }
  .postcard--back { left: 610px; }

  /* Front */
  .front__panel {
    position: absolute; left: 0; top: 0;
    width: 300px; height: 270px;
    background: var(--leaf);
  }
  .front__question { position: absolute; left: 0; top: 0; }
  .front__headline {
    position: absolute; left: 22px; top: 138px;
    width: 155px;
    color: var(--paper);
    font-size: 23px; line-height: 1.15; font-weight: 400;
  }
  .front__band {
    position: absolute; left: 0; bottom: 0;
    width: 300px; height: 90px;
    background: var(--leaf-dark);
    border-top: 4px solid var(--paper);
    display: flex; align-items: center;
    padding-left: 22px;
  }
  .front__boost {
    color: var(--paper);
    font-size: 26px; line-height: 1.1; font-weight: 400;
    width: 120px;
  }
  .front__dot {
    position: absolute; left: 185px; top: 236px;
    width: 30px; height: 30px; border-radius: 50%;
    background: var(--paper);
  }
  .front__photo {
    position: absolute; right: 24px; top: 22px;
    width: 190px; height: 130px;
    border-radius: 6px;
    background: linear-gradient(160deg, #f4f4f4 0%, #eaeaea 45%, #e9c3a8 75%, #c9dcae 100%);
  }
  .front__brand {
    position: absolute; left: 322px; top: 172px; width: 200px;
  }
  .brand-name {
    font-family: "Yellowtail", "Brush Script MT", cursive;
    color: var(--ink);
    font-size: 30px; line-height: 1.1;
  }
  .front__tagline { font-size: 12px; font-weight: 600; margin-top: 8px; }
  .front__message { font-size: 11.5px; line-height: 1.45; color: var(--muted); margin-top: 10px; }

  /* Back */
  .back__corner {
    position: absolute; right: 0; top: 0;
    width: 210px; height: 150px;
    background: var(--leaf);
  }
  .back__details {
    position: absolute; left: 34px; top: 120px; width: 260px;
  }
  .contact-list { list-style: none; margin-top: 18px; }
  .contact-list li {
    display: flex; align-items: center; gap: 8px;
    font-size: 12px; color: var(--muted); margin-bottom: 7px;
  }
  .contact-list svg { flex: none; }
  .back__divider {
    position: absolute; left: 300px; top: 180px;
    width: 1px; height: 150px; background: var(--rule);
  }
</style>
</head>
<body>

<section class="postcard postcard--front" aria-label="Postcard front">
  <div class="front__panel">
    <svg class="front__question" width="300" height="270" viewBox="0 0 300 270" aria-hidden="true">
      <path d="M92 100 C92 52 128 22 172 22 C222 22 256 52 256 88 C256 118 236 132 218 144 C204 154 200 168 200 180 L200 224"
            fill="none" stroke="#ffffff" stroke-width="28" stroke-linecap="butt"/>
    </svg>
    <p class="front__headline">Feel good and want to stay that way</p>
  </div>
  <div class="front__band"><p class="front__boost">Need a boost</p></div>
  <span class="front__dot" aria-hidden="true"></span>

  <div class="front__photo" role="img" aria-label="Cracked eggshell with a green sprout growing from it"></div>

  <div class="front__brand">
    <p class="brand-name">Meadowbrook Wellness</p>
    <p class="front__tagline">An Energy Medicine Clinic</p>
    <p class="front__message">It's time for your tune-up appointment at Meadowbrook Wellness.</p>
  </div>
</section>

<section class="postcard postcard--back" aria-label="Postcard back">
  <div class="back__corner"></div>
  <div class="back__details">
    <p class="brand-name">Meadowbrook Wellness</p>
    <ul class="contact-list">
      <li>
        <svg width="12" height="12" viewBox="0 0 24 24" aria-hidden="true"><path fill="#5f8f1f" d="M6.6 10.8a15 15 0 0 0 6.6 6.6l2.2-2.2c.3-.3.7-.4 1-.2 1.1.4 2.3.6 3.6.6.6 0 1 .4 1 1V20c0 .6-.4 1-1 1C10.6 21 3 13.4 3 4c0-.6.4-1 1-1h3.5c.6 0 1 .4 1 1 0 1.3.2 2.5.6 3.6.1.3 0 .7-.2 1z"/></svg>
        415.627.1943
      </li>
      <li>
        <svg width="12" height="12" viewBox="0 0 24 24" aria-hidden="true"><path fill="#5f8f1f" d="M3 5h18v14H3zm2 2v.5l7 4.5 7-4.5V7l-7 4.5z"/></svg>
        hello@meadowbrookwellness.com
      </li>
      <li>
        <svg width="12" height="12" viewBox="0 0 24 24" aria-hidden="true"><circle cx="12" cy="12" r="9" fill="none" stroke="#5f8f1f" stroke-width="2"/><path d="M3 12h18M12 3c3 3 3 15 0 18M12 3c-3 3-3 15 0 18" fill="none" stroke="#5f8f1f" stroke-width="1.6"/></svg>
        MeadowbrookWellness.com
      </li>
    </ul>
  </div>
  <span class="back__divider" aria-hidden="true"></span>
</section>

</body>
</html>
```